Business card design for Automotive workshop

We need a business card for a new automotive repair and tyre shop called Keelstone Prime Automotive located in New Zealand. We are a clean, modern and fresh workshop and company.

Front needs to feature logo,
my name:
Marlo Fitzgerald (director)

Address:
42 Tamsin Road
Whitianga 3510

Phone: 07 541 2298
Mobile: 027 419 5073
Email: office@keelstoneautomotive.co.nz
Website: keelstoneautomotive.co.nz

Back needs to feature an area to write down appointment details, date and time.

Also feature a list of jobs and work we do such as,
Vehicle Servicing
All Mechanical Repairs
Warrant of Fitness
Tyres & Wheel Alignments
Automotive Diagnostics
Automotive Parts & Supplies

```html
<!DOCTYPE html>
<html lang="en">
<head>
<meta charset="utf-8">
<title>Keelstone Prime Automotive – Business Card</title>
<link rel="stylesheet" href="https://fonts.googleapis.com/css2?family=Arimo:ital,wght@0,400;0,700;1,400;1,700&display=swap">
<style>
  :root {
    --red: #e31e24;
    --black: #161616;
    --charcoal: #1e1e1e;
    --white: #ffffff;
    --ink: #111111;
    --rule: #8a8a8a;
    --bg-top: #2e2e2e;
    --bg-bottom: #4a4a4a;
  }
  * { box-sizing: border-box; margin: 0; padding: 0; }
  html, body { width: 1200px; height: 1200px; overflow: hidden; }
  body {
    background: linear-gradient(180deg, var(--bg-top), var(--bg-bottom));
    font-family: "Arimo", Arial, sans-serif;
    position: relative;
  }
  .card {
    position: absolute;
    left: 170px;
    width: 860px;
    height: 491px;
    overflow: hidden;
    box-shadow: 0 10px 30px rgba(0,0,0,.45);
  }
  .card-front { top: 79px; background: linear-gradient(180deg, #1a1a1a, var(--charcoal)); }
  .card-back { top: 630px; background: var(--white); }

  .brand-name {
    position: absolute;
    font-weight: 700;
    text-transform: uppercase;
    letter-spacing: 2px;
    line-height: 1;
    color: var(--red);
  }
  .card-front .brand-name { right: 48px; top: 50px; font-size: 50px; text-align: right; }
  .card-back .brand-name { left: 0; right: 0; top: 42px; font-size: 46px; text-align: center; }
  .brand-name span { display: block; }
  .brand-name span + span { margin-top: 8px; }

  .holder {
    position: absolute;
    right: 450px;
    top: 228px;
    text-align: right;
  }
  .holder-name { color: var(--red); font-weight: 700; font-style: italic; font-size: 34px; }
  .holder-role { color: var(--white); font-style: italic; font-size: 22px; margin-top: 4px; }

  .divider { position: absolute; left: 430px; top: 218px; width: 1.5px; height: 118px; background: var(--white); }

  .contacts { position: absolute; left: 455px; top: 222px; list-style: none; }
  .contacts li {
    display: flex; align-items: center; gap: 10px;
    color: var(--white); font-style: italic; font-size: 21px; line-height: 29px;
  }
  .contacts svg { width: 15px; height: 15px; flex: none; }

  .address-band {
    position: absolute; left: 0; right: 0; top: 378px; height: 60px;
    background: var(--red);
    display: flex; align-items: center; justify-content: center;
    color: var(--white); font-style: italic; font-size: 24px;
  }

  .appointment-title {
    position: absolute; left: 0; right: 0; top: 168px; text-align: center;
    color: var(--red); font-weight: 700; font-size: 30px; letter-spacing: 1px;
  }
  .field { position: absolute; display: flex; align-items: flex-end; font-style: italic; font-size: 27px; color: var(--ink); }
  .field .line { flex: 1; border-bottom: 1.5px solid var(--rule); margin-left: 6px; height: 1px; }
  .field-date { left: 60px; top: 218px; width: 380px; }
  .rule-left { position: absolute; left: 60px; top: 290px; width: 360px; border-bottom: 1.5px solid var(--rule); }
  .field-time { left: 430px; top: 262px; width: 370px; }
  .rule-full { position: absolute; left: 60px; top: 320px; width: 740px; }

  .days { position: absolute; left: 78px; right: 60px; top: 322px; display: flex; justify-content: space-between; list-style: none; }
  .days li { display: flex; align-items: center; gap: 4px; font-size: 27px; color: var(--ink); }
  .days li::before {
    content: ""; width: 20px; height: 20px; border: 1.5px solid var(--red); border-radius: 50%;
  }

  .notice { position: absolute; left: 0; right: 0; top: 368px; text-align: center; font-size: 19px; color: var(--ink); }

  .services {
    position: absolute; left: 0; right: 0; bottom: 0; height: 86px;
    background: var(--black);
    border-top: 4px solid var(--red);
    display: flex; flex-direction: column; justify-content: center; align-items: center; gap: 6px;
    color: var(--white); font-size: 19px;
  }
  .services p { display: flex; gap: 10px; }
  .services span::before { content: "•"; color: var(--red); margin-right: 6px; }
</style>
</head>
<body>

<section class="card card-front" aria-label="Business card front">
  <div class="brand-name"><span>Keelstone Prime</span><span>Automotive</span></div>

  <div class="holder">
    <div class="holder-name">Marlo Fitzgerald</div>
    <div class="holder-role">Owner</div>
  </div>
  <div class="divider"></div>

  <ul class="contacts">
    <li><svg viewBox="0 0 16 16" aria-hidden="true"><path fill="#e31e24" d="M3.6 1.2l2.3 2.6-1.4 1.8c.9 2.1 2.6 3.8 4.8 4.8l1.8-1.4 2.6 2.3-1.3 2.4C7.4 13.6 2.4 8.6 1.2 3.6z"/></svg>07 541 2298</li>
    <li><svg viewBox="0 0 16 16" aria-hidden="true"><rect x="4" y="1" width="8" height="14" rx="1.5" fill="none" stroke="#e31e24" stroke-width="1.6"/><circle cx="8" cy="12.5" r=".9" fill="#e31e24"/></svg>027 419 5073</li>
    <li><svg viewBox="0 0 16 16" aria-hidden="true"><rect x="1" y="3" width="14" height="10" fill="#e31e24"/><path d="M1 3l7 6 7-6" fill="none" stroke="#161616" stroke-width="1.3"/></svg>office@keelstoneautomotive.co.nz</li>
    <li><svg viewBox="0 0 16 16" aria-hidden="true"><g fill="none" stroke="#e31e24" stroke-width="1.3"><circle cx="8" cy="8" r="6.5"/><ellipse cx="8" cy="8" rx="3" ry="6.5"/><path d="M1.5 8h13M2.5 4.8h11M2.5 11.2h11"/></g></svg>keelstoneautomotive.co.nz</li>
  </ul>

  <div class="address-band">42 Tamsin Road, Whitianga 3510</div>
</section>

<section class="card card-back" aria-label="Business card back">
  <div class="brand-name"><span>Keelstone Prime</span><span>Automotive</span></div>

  <div class="appointment-title">APPOINTMENT</div>

  <div class="field field-date">Date:<span class="line"></span></div>
  <div class="rule-left"></div>
  <div class="field field-time">Time:<span class="line"></span></div>

  <ul class="days">
    <li>Mon</li><li>Tue</li><li>Wed</li><li>Thur</li><li>Fri</li><li>Sat</li>
  </ul>

  <p class="notice">If you are unable to keep your appointment, please call us as soon as possible</p>

  <div class="services">
    <p><span>Vehicle Servicing</span><span>All Mechanical Repairs</span><span>Warrant of Fitness</span></p>
    <p><span>Tyres &amp; Wheel Alignments</span><span>Automotive Diagnostics</span><span>Automotive Parts &amp; Supplies</span></p>
  </div>
</section>

</body>
</html>
```